" Elaboramos soluções para que nossos clientes possam alocar adequadamente os recursos disponíveis (tempo, dinheiro, contatos, produtos, imagem, infra) em ações e iniciativas que tragam resultados efetivos e sustentáveis, alinhados aos seus valores, metas e partes interessadas. Desenvolvemos para eles projetos de investimentos, análises estratégicas, estudos de viabilidade, relatórios de avaliação e monitoramento, referências para formulação de políticas públicas, treinamentos, capacitações, reuniões, oficinas e tantos outras soluções. Acreditamos que o empreendedorismo e a inovação são mecanismos com os quais podemos apoiar o desenvolvimento sustentável local e regional. Nossa essência competitiva reside na proximidade e conexão para com todas as partes interessadas, compromisso com valores éticos e morais, inteligência, assertividade, inovação e aprendizado. Buscamos contato com as necessidades dos clientes desde o primeiro momento, garantindo que a construção das soluções respeite processos de diálogo contínuo. As principais características de nossos serviços são: - Informações e conhecimento confiáveis e aplicáveis; - Ações que gerem valores tangíveis e intangíveis positivos, especialmente no tocante à imagem e à confiabilidade; - Acesso a ideias, relacionamentos e oportunidades únicos; - Inovação. Considerados os elementos acima, é preciso destacar que toda a nossa atuação se dá em sintonia e parceria com cada indivíduo envolvido. Assim, consideramos as pessoas como fundamento e objetivo de nossa atuação. "

```html
<!DOCTYPE html>
<html lang="pt-BR">
<head>
<meta charset="utf-8">
<title>Manual de Identidade Visual — Vertente Plena</title>
<link rel="stylesheet" href="https://fonts.googleapis.com/css2?family=Raleway:wght@300;400&display=swap">
<style>
  :root {
    --stage: #b4b4b6;
    --cover-base: #f7f6f9;
    --tint-lilac: #e6dcef;
    --tint-teal: #d7ecef;
    --tint-green: #dff0dc;
    --title-violet: #75677f;
    --title-teal: #3d9eab;
    --title-green: #89be78;
    --brand: #4f7f97;
  }
  * { box-sizing: border-box; margin: 0; padding: 0; }
  html, body {
    width: 1200px;
    height: 1200px;
    overflow: hidden;
    background: var(--stage);
  }
  .canvas {
    width: 1200px;
    height: 1200px;
    display: flex;
    align-items: center;
    justify-content: center;
  }
  .cover {
    position: relative;
    width: 706px;
    height: 1000px;
    background: var(--cover-base);
    overflow: hidden;
    font-family: "Raleway", sans-serif;
  }
  .cover-pattern {
    position: absolute;
    inset: 0;
    background:
      linear-gradient(155deg, rgba(255,255,255,0.9) 0%, rgba(255,255,255,0) 45%),
      linear-gradient(200deg, var(--tint-lilac) 0%, rgba(230,220,239,0) 55%),
      linear-gradient(30deg, var(--tint-teal) 0%, rgba(215,236,239,0) 50%),
      linear-gradient(330deg, var(--tint-green) 0%, rgba(223,240,220,0) 45%),
      linear-gradient(180deg, #f4f1f7 0%, #ece5f1 60%, #e3eef0 100%);
  }
  .manual-title {
    position: absolute;
    top: 178px;
    left: 0;
    right: 0;
    text-align: center;
    font-weight: 300;
    font-size: 50px;
    line-height: 62px;
    letter-spacing: 1px;
  }
  .manual-title span { display: block; }
  .manual-title .line-manual { color: var(--title-violet); }
  .manual-title .line-identity { color: var(--title-teal); }
  .manual-title .line-visual { color: var(--title-green); }
  .brand-name {
    position: absolute;
    top: 770px;
    left: 0;
    right: 0;
    text-align: center;
    font-weight: 300;
    font-size: 78px;
    color: var(--brand);
  }
</style>
</head>
<body>
  <main class="canvas">
    <section class="cover">
      <div class="cover-pattern" role="img" aria-label="Padrão de formas geométricas translúcidas em tons de lilás, azul-piscina e verde claro"></div>
      <h1 class="manual-title">
        <span class="line-manual">MANUAL DE</span>
        <span class="line-identity">IDENTIDADE</span>
        <span class="line-visual">VISUAL</span>
      </h1>
      <p class="brand-name">Vertente Plena</p>
    </section>
  </main>
</body>
</html>
```